Cedar Lantern Gazette Website Redesign to Better Access Local News and distribute it to more people

I currently have the local news website www.cedarlanterngazette.com and am seeking a new front page design that will update the main page and make it more current and user friendly, including ways to post to the sight from my cell phone, connectivity to friendloop, chirpwave, and snapmosaic accounts and other updates to provide clients with a "new face" and updated way of getting their news. It's been approximately 10 years since I've updated the main page and I know that it needs a fresh new look.

I'm a professional photographer, thus I want to highlight my photography work on a daily basis and offer photographs for the public to enjoy, as this has been a "drawing point" over other local media outlets.

The website is locally know for providing numerous photos of local news events and giving the public access to seeing themselves in the news.

You can also access my friendloop page cedarlantern gazette and see additional content that I provide there for over 17000 friends and followers.

I want a way to archive old material, for future access, but to "cut down" on the clutter of the page.

I also want to keep the way that I can sell advertising at the current ad levels but would also like to sell additional space on the sides of the front page, for increase revenue.

I currently update the website with vellum-works composer, daily.

I have some ideas in mind, but am open to new and fresh ideas and ways to make it more user friendly. If you have any questions, please message me and I'll try to explain more fully.

Target Market(s)

Public as a news source

Industry/Entity Type

News

Coding

Coded - Design and coding required

Number of Pages Required

1 page

Font styles to use
Sans Serif

Requirements
Must have
• Ways to upload material from friendloop, a way to post three photos each day that are changed out daily and ways to automatically archive old material. Must look good on cell phones.
Nice to have
• Anything that would streamline news feed and make it easier accessible to other media.
Should not have
• Open.

```html
<!DOCTYPE html>
<html lang="en">
<head>
<meta charset="utf-8">
<title>Cedar Lantern Gazette — Local News</title>
<link rel="stylesheet" href="https://fonts.googleapis.com/css2?family=Open+Sans:wght@400;600;700&family=Roboto+Condensed:wght@400;700&display=swap">
<style>
:root{
  --red:#d3141b;
  --red-dark:#a80f15;
  --navy:#1b2542;
  --ink:#333;
  --muted:#888;
  --line:#e2e2e2;
  --page:#efefef;
  --card:#ffffff;
}
*{box-sizing:border-box;margin:0;padding:0}
html,body{width:1200px;height:3876px;overflow:hidden}
body{background:var(--page);font-family:"Open Sans",Arial,sans-serif;color:var(--ink);font-size:12px;line-height:1.45;position:relative}
a{color:inherit;text-decoration:none}
ul{list-style:none}

.topbar{height:40px;background:var(--navy);display:flex;align-items:center;padding:0 50px;gap:14px;color:#fff}
.topbar__label{background:var(--red);padding:4px 10px;font-weight:700;font-size:11px}
.topbar__ticker{font-size:11px;flex:1}
.topbar__social{display:flex;gap:8px}
.topbar__social span{width:16px;height:16px;border-radius:50%;background:#fff;opacity:.85}

.masthead{height:136px;background:var(--card);display:flex;align-items:center;justify-content:center}
.brand{display:flex;align-items:center;gap:12px;font-family:"Roboto Condensed",sans-serif;font-weight:700;font-size:34px;color:var(--red)}
.brand__mark{width:22px;height:22px;border-radius:50%;background:var(--navy)}

.mainnav{height:44px;background:var(--red);display:flex;align-items:center;padding:0 50px}
.mainnav__home{width:44px;height:44px;background:var(--red-dark);display:flex;align-items:center;justify-content:center}
.mainnav ul{display:flex;flex:1}
.mainnav li{color:#fff;font-family:"Roboto Condensed",sans-serif;font-weight:700;font-size:15px;padding:0 18px;line-height:44px;border-right:1px solid rgba(255,255,255,.25)}
.mainnav__search{width:44px;height:44px;background:var(--navy);display:flex;align-items:center;justify-content:center}

.wrap{width:1100px;margin:0 auto}
.ph{display:block;border-radius:0}

.slider{margin-top:12px;height:408px;display:flex;gap:8px;position:relative}
.slide{position:relative;height:100%}
.slide--main{width:640px}
.slide--side{flex:1}
.slide__caption{position:absolute;left:0;right:0;bottom:0;background:rgba(20,24,40,.78);padding:14px 18px;color:#fff}
.slide__title{font-family:"Roboto Condensed",sans-serif;font-weight:700;font-size:24px;color:#fff;border-left:4px solid var(--red);padding-left:10px;margin-bottom:4px}
.slide__text{font-size:12px;color:#ddd}
.slider__arrow{position:absolute;top:180px;width:30px;height:40px;background:#fff;display:flex;align-items:center;justify-content:center}

.layout{display:flex;gap:30px;margin-top:32px}
.main{width:740px}
.side{width:330px;display:flex;flex-direction:column;gap:22px}

.block{background:var(--card);padding:14px}
.sec-head{display:flex;align-items:center;justify-content:space-between;border-bottom:2px solid var(--red);margin-bottom:12px}
.sec-head__label{background:var(--red);color:#fff;font-family:"Roboto Condensed",sans-serif;font-weight:700;font-size:14px;text-transform:uppercase;padding:6px 12px}
.sec-head__more{width:24px;height:24px;background:var(--navy);color:#fff;display:flex;align-items:center;justify-content:center;font-weight:700;font-size:16px;margin-bottom:2px}

.cols{display:flex;gap:20px}
.cols>*{flex:1;min-width:0}
.item{display:flex;gap:10px;padding:8px 0;border-bottom:1px solid var(--line)}
.item__thumb{width:72px;height:54px;flex:none}
.item__title{color:var(--red);font-weight:700;font-size:12px;line-height:1.3}
.item__meta{color:var(--muted);font-size:10px;margin:2px 0}
.item__text{font-size:11px;color:#555}

.lead__img{height:190px}
.lead__title{color:var(--red);font-weight:700;font-size:14px;margin-top:10px}

.ads{display:grid;grid-template-columns:repeat(3,1fr);gap:10px}
.ads .ph{height:112px}

.grid4{display:grid;grid-template-columns:repeat(4,1fr);gap:12px}
.grid4 .ph{height:150px}
.card__title{color:var(--red);font-weight:700;font-size:13px;margin-top:8px;line-height:1.3}

.mosaic{display:grid;grid-template-columns:180px 1fr;grid-template-rows:128px 128px;gap:8px}
.mosaic__big{grid-row:1/3;grid-column:2;position:relative}
.mosaic__tile{position:relative}
.overlay{position:absolute;left:0;right:0;bottom:0;background:rgba(20,24,40,.75);color:#fff;padding:8px 10px;font-size:12px;font-weight:700}
.overlay small{display:block;font-weight:400;font-size:10px;color:#ccc}

.search{display:flex;height:36px;background:#fff;border:1px solid var(--line)}
.search span{flex:1;padding:8px 12px;color:var(--muted)}
.search i{width:36px;background:var(--red);display:flex;align-items:center;justify-content:center}

.tabs{display:flex;margin-bottom:10px}
.tabs span{flex:1;text-align:center;background:var(--navy);color:#fff;font-family:"Roboto Condensed",sans-serif;font-weight:700;padding:7px 0;font-size:13px}
.tabs span.is-active{background:var(--red)}

.widget{border:1px solid var(--line);padding:10px}
.widget__head{display:flex;gap:10px;align-items:center;margin-bottom:10px}
.widget__head .ph{width:50px;height:50px}
.widget__name{font-weight:700;color:var(--navy)}
.widget__btn{display:inline-block;border:1px solid #ccc;padding:2px 8px;font-size:10px;margin-top:4px}
.faces{display:grid;grid-template-columns:repeat(6,1fr);gap:5px}
.faces span{height:40px;background:linear-gradient(#b9c4d2,#8c9bb0)}

.footer{position:absolute;left:0;right:0;top:3520px;height:356px;background:#fafafa;border-top:4px solid var(--red)}
.footer__cols{display:flex;gap:30px;padding-top:28px}
.footer__col{flex:1;min-width:0}
.footer__head{font-family:"Roboto Condensed",sans-serif;font-weight:700;text-transform:uppercase;color:var(--red);font-size:14px;border-bottom:1px solid var(--line);padding-bottom:6px;margin-bottom:12px}
.footer__brand{font-family:"Roboto Condensed",sans-serif;font-weight:700;font-size:22px;color:var(--red);margin-bottom:10px}
.footer li{padding:4px 0;border-bottom:1px dotted var(--line)}
.contact{display:flex;gap:8px;align-items:flex-start;margin-bottom:10px}
.social-dots{display:flex;gap:8px;margin-bottom:18px}
.social-dots span{width:28px;height:28px;border-radius:50%;background:var(--navy)}
.newsletter{display:flex;height:32px;border:1px solid var(--line);background:#fff}
.newsletter span{flex:1;padding:6px 10px;color:var(--muted)}
.newsletter b{background:var(--red);color:#fff;padding:6px 12px;font-weight:600}
.copyright{position:absolute;bottom:0;left:0;right:0;height:40px;background:#eaeaea;text-align:center;line-height:40px;color:var(--muted);font-size:11px}
</style>
</head>
<body>

<div class="topbar">
  <span class="topbar__label">Latest News</span>
  <span class="topbar__ticker">Town Council approves new park benches for downtown square</span>
  <div class="topbar__social"><span></span><span></span><span></span><span></span><span></span></div>
</div>

<header class="masthead">
  <div class="brand"><span class="brand__mark"></span>Cedar Lantern Gazette</div>
</header>

<nav class="mainnav">
  <div class="mainnav__home"><svg width="18" height="18" viewBox="0 0 18 18"><path d="M2 9 9 3l7 6v7h-5v-4H7v4H2z" fill="#fff"/></svg></div>
  <ul>
    <li>Birthdays &amp; History</li><li>Obituaries</li><li>General Store</li><li>Archive Local News</li><li>Community Events</li><li>Sports News</li><li>More ▾</li>
  </ul>
  <div class="mainnav__search"><svg width="16" height="16" viewBox="0 0 16 16"><circle cx="6.5" cy="6.5" r="5" stroke="#fff" stroke-width="2" fill="none"/><path d="m10.5 10.5 4 4" stroke="#fff" stroke-width="2"/></svg></div>
</nav>

<div class="wrap">
  <section class="slider">
    <div class="slide slide--main">
      <div class="ph" style="height:100%;background:linear-gradient(135deg,#8fa3b8,#4c5a6e)" role="img" aria-label="News photo of a reporter team filming an interview outdoors"></div>
      <div class="slide__caption"><div class="slide__title">Cedar Lantern Gazette</div><div class="slide__text">Lorem ipsum dolor sit amet, consectetur adipiscing elit. Sed commodo lectus sit amet bibendum, in sodales ipsum tristique.</div></div>
    </div>
    <div class="slide slide--side">
      <div class="ph" style="height:100%;background:linear-gradient(160deg,#c9a98f,#6d4a3c)" role="img" aria-label="Photo of the festival pageant winner wearing a crown"></div>
      <div class="slide__caption"><div class="slide__title">Maple Dairy Festival</div><div class="slide__text">Lorem ipsum dolor sit amet, consectetur adipiscing elit. Sed commodo lectus sit amet bibendum.</div></div>
    </div>
    <span class="slider__arrow" style="left:0"><svg width="10" height="14"><path d="M8 1 2 7l6 6" stroke="#333" stroke-width="2" fill="none"/></svg></span>
    <span class="slider__arrow" style="left:610px"><svg width="10" height="14"><path d="m2 1 6 6-6 6" stroke="#333" stroke-width="2" fill="none"/></svg></span>
  </section>

  <div class="layout">
    <main class="main">
      <section class="block" style="height:560px">
        <div class="cols">
          <div>
            <div class="sec-head"><span class="sec-head__label">Local News</span><span class="sec-head__more">+</span></div>
            <div class="item"><span class="ph item__thumb" style="background:linear-gradient(#9cc46a,#5c8a34)" role="img" aria-label="Local business sign photo"></span><div><div class="item__title">Lorem Ipsum Dolor sit ametfour</div><div class="item__meta">Posted on 15 Sept 2015 · 0 Comments</div><div class="item__text">Fresh &amp; fab arrangements at the downtown flower market.</div></div></div>
            <div class="item"><span class="ph item__thumb" style="background:linear-gradient(#c7a27a,#7f5b3a)" role="img" aria-label="Town event photo"></span><div><div class="item__title">Lorem Ipsum Dolor sit ametfour</div><div class="item__meta">Posted on 15 Sept 2015 · 0 Comments</div><div class="item__text">Senior Care Plan advice: what to check this year.</div></div></div>
            <div class="item"><span class="ph item__thumb" style="background:linear-gradient(#e0b86a,#a8742c)" role="img" aria-label="Kayaking outing photo"></span><div><div class="item__title">Good morning Kayaking</div><div class="item__meta">Posted on 15 Sept 2015 · 0 Comments</div><div class="item__text">Paddlers gather at the lake for the early season launch.</div></div></div>
            <div class="item"><span class="ph item__thumb" style="background:linear-gradient(#b3b9c4,#6a7281)" role="img" aria-label="Community meeting photo"></span><div><div class="item__title">Lorem Ipsum Dolor sit ametfour</div><div class="item__meta">Posted on 15 Sept 2015 · 0 Comments</div><div class="item__text">County Campus Safety Circle meets in town.</div></div></div>
            <div class="item"><span class="ph item__thumb" style="background:linear-gradient(#a9c79a,#5f7d52)" role="img" aria-label="Outdoor gathering photo"></span><div><div class="item__title">Lorem Ipsum Dolor sit ametfour</div><div class="item__meta">Posted on 15 Sept 2015 · 0 Comments</div><div class="item__text">Southern Harvest Fair returns this coming weekend.</div></div></div>
          </div>
          <div>
            <div class="sec-head"><span class="sec-head__label">Texas Our Texas</span><span class="sec-head__more">+</span></div>
            <div class="item"><span class="ph item__thumb" style="background:linear-gradient(#a8b6cc,#3d4e72)" role="img" aria-label="State flag photo"></span><div><div class="item__title">Lorem Ipsum Dolor sit ametfour</div><div class="item__meta">Posted on 15 Sept 2015 · 0 Comments</div><div class="item__text">Historic marker unveiled near the county courthouse.</div></div></div>
            <div class="item"><span class="ph item__thumb" style="background:linear-gradient(#d3b08b,#8d6a49)" role="img" aria-label="Ranch landscape photo"></span><div><div class="item__title">Lorem Ipsum Dolor sit ametfour</div><div class="item__meta">Posted on 15 Sept 2015 · 0 Comments</div><div class="item__text">Ranch families share stories of the long dry summer.</div></div></div>
            <div class="item"><span class="ph item__thumb" style="background:linear-gradient(#8fa58a,#4a6245)" role="img" aria-label="Courthouse photo"></span><div><div class="item__title">Fall Season Show Current Edition</div><div class="item__meta">Posted on 15 Sept 2015 · 0 Comments</div><div class="item__text">Artists gather for the annual fall season showcase.</div></div></div>
            <div class="item"><span class="ph item__thumb" style="background:linear-gradient(#c9a46e,#86622f)" role="img" aria-label="Roadside stand photo"></span><div><div class="item__title">The Hen House Stand</div><div class="item__meta">Posted on 15 Sept 2015 · 0 Comments</div><div class="item__text">New farm stand opens along the old county road.</div></div></div>
            <div class="item"><span class="ph item__thumb" style="background:linear-gradient(#b0bac6,#5e6878)" role="img" aria-label="Town street photo"></span><div><div class="item__title">Lorem Ipsum Dolor sit ametfour</div><div class="item__meta">Posted on 15 Sept 2015 · 0 Comments</div><div class="item__text">Main street repaving starts on Monday morning.</div></div></div>
          </div>
        </div>
      </section>

      <section class="block" style="height:300px;margin-top:24px">
        <div class="sec-head"><span class="sec-head__label">Pellentesque News</span><span class="sec-head__more">+</span></div>
        <div class="ads">
          <span class="ph" style="background:linear-gradient(135deg,#f2d24a,#e07b2b)" role="img" aria-label="Advertisement banner for a local pizza shop"></span>
          <span class="ph" style="background:linear-gradient(135deg,#e8e2d6,#b9a88a)" role="img" aria-label="Advertisement banner for a local service"></span>
          <span class="ph" style="background:linear-gradient(135deg,#d9e6f2,#8aa6c4)" role="img" aria-label="Advertisement banner for a regional business"></span>
          <span class="ph" style="background:linear-gradient(135deg,#6b3f27,#2b1a12)" role="img" aria-label="Advertisement banner for a restaurant"></span>
          <span class="ph" style="background:linear-gradient(135deg,#c94a2c,#f0a04a)" role="img" aria-label="Advertisement banner for a grocery store"></span>
          <span class="ph" style="background:linear-gradient(135deg,#c7d5e6,#5c7ba3)" role="img" aria-label="Advertisement banner for an auto dealer"></span>
        </div>
      </section>

      <section class="block" style="height:700px;margin-top:24px">
        <div class="cols">
          <div>
            <div class="sec-head"><span class="sec-head__label">Our Sport News</span><span class="sec-head__more">+</span></div>
            <div class="ph lead__img" style="background:linear-gradient(#9ebee0,#5a8a3e)" role="img" aria-label="Photo of a high school football game"></div>
            <div class="lead__title">A Second Length Title With Little Text</div>
            <div class="item__meta">Posted on 15 Sept 2015 · 0 Comments</div>
            <div class="item__text">Fresh &amp; fab arrangements as the home team wins the regional opener.</div>
            <div class="item"><span class="ph item__thumb" style="background:linear-gradient(#a6b4c4,#56657a)" role="img" aria-label="Sports team photo"></span><div><div class="item__title">Lorem Ipsum Dolor sit ametfour</div><div class="item__meta">Posted on 15 Sept 2015 · 0 Comments</div><div class="item__text">Coach names starters for Friday night.</div></div></div>
            <div class="item"><span class="ph item__thumb" style="background:linear-gradient(#c3a07c,#7c5a3a)" role="img" aria-label="Baseball photo"></span><div><div class="item__title">Lorem Ipsum Dolor sit ametfour</div><div class="item__meta">Posted on 15 Sept 2015 · 0 Comments</div><div class="item__text">Youth league signups open this week.</div></div></div>
            <div class="item"><span class="ph item__thumb" style="background:linear-gradient(#9bc08a,#4f7a40)" role="img" aria-label="Track meet photo"></span><div><div class="item__title">Lorem Ipsum Dolor sit ametfour</div><div class="item__meta">Posted on 15 Sept 2015 · 0 Comments</div><div class="item__text">Runners qualify for the state meet.</div></div></div>
            <div class="item"><span class="ph item__thumb" style="background:linear-gradient(#b7b7c7,#676781)" role="img" aria-label="Volleyball photo"></span><div><div class="item__title">Lorem Ipsum Dolor sit ametfour</div><div class="item__meta">Posted on 15 Sept 2015 · 0 Comments</div><div class="item__text">Home volleyball team sweeps district rival.</div></div></div>
          </div>
          <div>
            <div class="sec-head"><span class="sec-head__label">Church News</span><span class="sec-head__more">+</span></div>
            <div class="ph lead__img" style="background:linear-gradient(#bcd3ea,#e9ecef 60%,#7c9a5c)" role="img" aria-label="Photo of a white country church"></div>
            <div class="lead__title">A Second Length Title With Little Text</div>
            <div class="item__meta">Posted on 15 Sept 2015 · 0 Comments</div>
            <div class="item__text">Fresh &amp; fab arrangements for the autumn revival services.</div>
            <div class="item"><span class="ph item__thumb" style="background:linear-gradient(#d6c4a8,#93795a)" role="img" aria-label="Church interior photo"></span><div><div class="item__title">Lorem Ipsum Dolor sit ametfour</div><div class="item__meta">Posted on 15 Sept 2015 · 0 Comments</div><div class="item__text">Congregation celebrates its anniversary.</div></div></div>
            <div class="item"><span class="ph item__thumb" style="background:linear-gradient(#a9bcd0,#5c7088)" role="img" aria-label="Choir photo"></span><div><div class="item__title">Lorem Ipsum Dolor sit ametfour</div><div class="item__meta">Posted on 15 Sept 2015 · 0 Comments</div><div class="item__text">Community choir plans holiday concert.</div></div></div>
            <div class="item"><span class="ph item__thumb" style="background:linear-gradient(#c9b08f,#7e6548)" role="img" aria-label="Church supper photo"></span><div><div class="item__title">Lorem Ipsum Dolor sit ametfour</div><div class="item__meta">Posted on 15 Sept 2015 · 0 Comments</div><div class="item__text">Potluck supper raises funds for repairs.</div></div></div>
            <div class="item"><span class="ph item__thumb" style="background:linear-gradient(#b2c4a6,#627857)" role="img" aria-label="Chapel photo"></span><div><div class="item__title">Lorem Ipsum Dolor sit ametfour</div><div class="item__meta">Posted on 15 Sept 2015 · 0 Comments</div><div class="item__text">Youth group returns from mission trip.</div></div></div>
          </div>
        </div>
      </section>

      <section class="block" style="height:360px;margin-top:24px">
        <div class="sec-head"><span class="sec-head__label">Pellentesque News</span><span class="sec-head__more">+</span></div>
        <div class="grid4">
          <div><span class="ph" style="background:linear-gradient(#9fc4e8,#e2783a)" role="img" aria-label="Hot air balloons photo"></span><div class="card__title">This Is Going To Be A Second Length Title With Little Text</div><div class="item__meta">Posted on 15 Sept 2015</div><div class="item__text">Lorem ipsum dolor sit amet, consectetur elit.</div></div>
          <div><span class="ph" style="background:linear-gradient(#c73a2c,#e6a04a)" role="img" aria-label="Fresh apples photo"></span><div class="card__title">This Is Going To Be A Second Length Title With Little Text</div><div class="item__meta">Posted on 15 Sept 2015</div><div class="item__text">Lorem ipsum dolor sit amet, consectetur elit.</div></div>
          <div><span class="ph" style="background:linear-gradient(#e8c06a,#b25a2a)" role="img" aria-label="Citrus fruit photo"></span><div class="card__title">This Is Going To Be A Second Length Title With Little Text</div><div class="item__meta">Posted on 15 Sept 2015</div><div class="item__text">Lorem ipsum dolor sit amet, consectetur elit.</div></div>
          <div><span class="ph" style="background:linear-gradient(#d7ccbc,#8f7d66)" role="img" aria-label="Bakery goods photo"></span><div class="card__title">This Is Going To Be A Second Length Title With Little Text</div><div class="item__meta">Posted on 15 Sept 2015</div><div class="item__text">Lorem ipsum dolor sit amet, consectetur elit.</div></div>
        </div>
      </section>

      <section class="block" style="height:330px;margin-top:24px">
        <div class="sec-head"><span class="sec-head__label">Pellentesque Post</span><span class="sec-head__more">+</span></div>
        <div class="mosaic">
          <div class="mosaic__tile"><span class="ph" style="height:100%;background:linear-gradient(#8fb0d8,#b84a3a)" role="img" aria-label="Flag and building photo"></span><div class="overlay">Decent Title With Little Text<small>15 Sept 2015</small></div></div>
          <div class="mosaic__tile" style="grid-row:2"><span class="ph" style="height:100%;background:linear-gradient(#c9b48d,#6d5a3d)" role="img" aria-label="Town square photo"></span><div class="overlay">Decent Title With Little Text<small>15 Sept 2015</small></div></div>
          <div class="mosaic__big"><span class="ph" style="height:100%;background:linear-gradient(135deg,#8a2a2a,#d6a44a 60%,#3a2a2a)" role="img" aria-label="Photo of a costumed performer on stage"></span><div class="overlay" style="font-size:14px">This Is Going To Be A Second Length Title With Little Text<small>Lorem ipsum dolor sit amet, consectetur adipiscing elit, sed do eiusmod.</small></div></div>
        </div>
      </section>

      <section class="block" style="height:370px;margin-top:24px">
        <div class="cols">
          <div>
            <div class="sec-head"><span class="sec-head__label">Pellentesque News</span><span class="sec-head__more">+</span></div>
            <div class="ph" style="height:150px;background:linear-gradient(#d4c2a6,#8c7552)" role="img" aria-label="Photo of volunteers unloading boxes"></div>
            <div class="lead__title">This Is Going To Be A Second Length Title With Little Text</div>
            <div class="item__meta">Posted on 15 Sept 2015 · 0 Comments</div>
            <div class="item__text">Lorem ipsum dolor sit amet, consectetur adipiscing elit. Integer nec odio praesent libero sed cursus ante dapibus diam sed nisi nulla quis sem at nibh elementum imperdiet duis sagittis.</div>
          </div>
          <div>
            <div class="sec-head"><span class="sec-head__label">Pellentesque News</span><span class="sec-head__more">+</span></div>
            <div class="item"><span class="ph item__thumb" style="background:linear-gradient(#c7a27a,#7f5b3a)" role="img" aria-label="News photo"></span><div><div class="item__title">Lorem Ipsum Dolor sit ametfour</div><div class="item__meta">Posted on 15 Sept 2015 · 0 Comments</div><div class="item__text">Library extends weekend reading hours.</div></div></div>
            <div class="item"><span class="ph item__thumb" style="background:linear-gradient(#a6b4c4,#56657a)" role="img" aria-label="News photo"></span><div><div class="item__title">Lorem Ipsum Dolor sit ametfour</div><div class="item__meta">Posted on 15 Sept 2015 · 0 Comments</div><div class="item__text">Fire department hosts open house.</div></div></div>
            <div class="item"><span class="ph item__thumb" style="background:linear-gradient(#9bc08a,#4f7a40)" role="img" aria-label="News photo"></span><div><div class="item__title">Lorem Ipsum Dolor sit ametfour</div><div class="item__meta">Posted on 15 Sept 2015 · 0 Comments</div><div class="item__text">Garden club awards yard of the month.</div></div></div>
            <div class="item"><span class="ph item__thumb" style="background:linear-gradient(#d6b8a0,#8a6650)" role="img" aria-label="News photo"></span><div><div class="item__title">Lorem Ipsum Dolor sit ametfour</div><div class="item__meta">Posted on 15 Sept 2015 · 0 Comments</div><div class="item__text">Senior center plans autumn dance.</div></div></div>
          </div>
        </div>
      </section>
    </main>

    <aside class="side">
      <div class="search"><span>Search here...</span><i><svg width="14" height="14" viewBox="0 0 16 16"><circle cx="6.5" cy="6.5" r="5" stroke="#fff" stroke-width="2" fill="none"/><path d="m10.5 10.5 4 4" stroke="#fff" stroke-width="2"/></svg></i></div>

      <section class="block">
        <div class="sec-head"><span class="sec-head__label">Photography Work</span><span class="sec-head__more">+</span></div>
        <div style="position:relative"><span class="ph" style="height:200px;background:linear-gradient(135deg,#5a7fc4,#a05ab0)" role="img" aria-label="Featured daily photograph"></span><div class="overlay" style="text-align:center">Watch Our Photography Work</div></div>
      </section>

      <section class="block">
        <div class="sec-head"><span class="sec-head__label">Pellentesque News</span><span class="sec-head__more">+</span></div>
        <div class="item"><span class="ph item__thumb" style="background:linear-gradient(#b7a58c,#6e5d46)" role="img" aria-label="News photo"></span><div><div class="item__title">Lorem Ipsum Dolor sit amet</div><div class="item__meta">15 Sept 2015 · 0 Comments</div><div class="item__text">Lorem ipsum dolor sit amet elit.</div></div></div>
        <div class="item"><span class="ph item__thumb" style="background:linear-gradient(#c39a8a,#7a4f42)" role="img" aria-label="News photo"></span><div><div class="item__title">Lorem Ipsum Dolor sit amet</div><div class="item__meta">15 Sept 2015 · 0 Comments</div><div class="item__text">Lorem ipsum dolor sit amet elit.</div></div></div>
        <div class="item"><span class="ph item__thumb" style="background:linear-gradient(#a7b8a0,#5c7054)" role="img" aria-label="News photo"></span><div><div class="item__title">Lorem Ipsum Dolor sit amet</div><div class="item__meta">15 Sept 2015 · 0 Comments</div><div class="item__text">Lorem ipsum dolor sit amet elit.</div></div></div>
        <div class="item"><span class="ph item__thumb" style="background:linear-gradient(#d1b890,#8e7147)" role="img" aria-label="News photo"></span><div><div class="item__title">Lorem Ipsum Dolor sit amet</div><div class="item__meta">15 Sept 2015 · 0 Comments</div><div class="item__text">Lorem ipsum dolor sit amet elit.</div></div></div>
        <div class="item"><span class="ph item__thumb" style="background:linear-gradient(#a9b4c6,#5b6a80)" role="img" aria-label="News photo"></span><div><div class="item__title">Lorem Ipsum Dolor sit amet</div><div class="item__meta">15 Sept 2015 · 0 Comments</div><div class="item__text">Lorem ipsum dolor sit amet elit.</div></div></div>
      </section>

      <section class="block">
        <div class="tabs"><span class="is-active">Recent</span><span>Popular</span><span>Random</span></div>
        <div class="item"><span class="ph item__thumb" style="background:linear-gradient(#c8a88a,#7e5d42)" role="img" aria-label="News photo"></span><div><div class="item__title">Lorem Ipsum Dolor sit amet</div><div class="item__meta">15 Sept 2015 · 0 Comments</div><div class="item__text">Lorem ipsum dolor sit amet elit.</div></div></div>
        <div class="item"><span class="ph item__thumb" style="background:linear-gradient(#b5c2a4,#66765a)" role="img" aria-label="News photo"></span><div><div class="item__title">Lorem Ipsum Dolor sit amet</div><div class="item__meta">15 Sept 2015 · 0 Comments</div><div class="item__text">Lorem ipsum dolor sit amet elit.</div></div></div>
        <div class="item"><span class="ph item__thumb" style="background:linear-gradient(#d2b4a0,#88604a)" role="img" aria-label="News photo"></span><div><div class="item__title">Lorem Ipsum Dolor sit amet</div><div class="item__meta">15 Sept 2015 · 0 Comments</div><div class="item__text">Lorem ipsum dolor sit amet elit.</div></div></div>
        <div class="item"><span class="ph item__thumb" style="background:linear-gradient(#a8b6c8,#596a82)" role="img" aria-label="News photo"></span><div><div class="item__title">Lorem Ipsum Dolor sit amet</div><div class="item__meta">15 Sept 2015 · 0 Comments</div><div class="item__text">Lorem ipsum dolor sit amet elit.</div></div></div>
      </section>

      <section class="block">
        <div class="sec-head"><span class="sec-head__label">Current Obituaries</span><span class="sec-head__more">+</span></div>
        <div class="widget">
          <div class="widget__head"><span class="ph" style="background:linear-gradient(#c7cfdb,#8a97ab)" role="img" aria-label="Page profile picture"></span><div><div class="widget__name">Cedar Lantern Newsroom</div><div class="item__meta">17,024 likes</div><span class="widget__btn">Like Page</span></div></div>
          <div class="faces"><span></span><span></span><span></span><span></span><span></span><span></span><span></span><span></span><span></span><span></span><span></span><span></span></div>
          <div class="item__meta" style="margin-top:8px">friendloop social plugin</div>
        </div>
      </section>

      <section class="block">
        <div class="sec-head"><span class="sec-head__label">Hot Post</span><span class="sec-head__more">+</span></div>
        <div class="item"><span class="ph item__thumb" style="background:linear-gradient(#d8b8a0,#8c6a52)" role="img" aria-label="News photo"></span><div><div class="item__title">Lorem Ipsum Dolor sit amet</div><div class="item__meta">15 Sept 2015 · 0 Comments</div></div></div>
        <div class="item"><span class="ph item__thumb" style="background:linear-gradient(#aebcd0,#5e6f88)" role="img" aria-label="News photo"></span><div><div class="item__title">Lorem Ipsum Dolor sit amet</div><div class="item__meta">15 Sept 2015 · 0 Comments</div></div></div>
        <div class="item"><span class="ph item__thumb" style="background:linear-gradient(#b6c8a4,#627a52)" role="img" aria-label="News photo"></span><div><div class="item__title">Lorem Ipsum Dolor sit amet</div><div class="item__meta">15 Sept 2015 · 0 Comments</div></div></div>
      </section>

      <section class="block">
        <div class="sec-head"><span class="sec-head__label">Our Videos</span><span class="sec-head__more">+</span></div>
        <div style="position:relative"><span class="ph" style="height:170px;background:linear-gradient(#7fa0c8,#3c5a7e)" role="img" aria-label="Video still of a local event"></span>
          <svg style="position:absolute;left:135px;top:55px" width="56" height="56" viewBox="0 0 56 56"><circle cx="28" cy="28" r="26" fill="rgba(0,0,0,.5)"/><path d="M22 17v22l18-11z" fill="#fff"/></svg></div>
      </section>

      <span class="ph" style="height:210px;background:linear-gradient(135deg,#f3c6d4,#e88aa8)" role="img" aria-label="Advertisement: expecting a baby maternity care offer"></span>
    </aside>
  </div>
</div>

<footer class="footer">
  <div class="wrap footer__cols">
    <div class="footer__col">
      <div class="footer__head">About Cedar Lantern</div>
      <div class="footer__brand">Cedar Lantern Gazette</div>
      <p>Lorem ipsum dolor sit amet, consectetur adipiscing elit. Integer nec odio praesent libero sed cursus ante dapibus diam sed nisi.</p>
    </div>
    <div class="footer__col">
      <div class="footer__head">Navigation</div>
      <ul><li>Home</li><li>About us</li><li>E-paper</li><li>Services</li><li>Portfolio</li><li>Contact us</li></ul>
    </div>
    <div class="footer__col">
      <div class="footer__head">Get In Touch</div>
      <div class="contact"><svg width="14" height="16" viewBox="0 0 14 16"><path d="M7 1a5 5 0 0 1 5 5c0 4-5 9-5 9S2 10 2 6a5 5 0 0 1 5-5z" fill="#d3141b"/><circle cx="7" cy="6" r="2" fill="#fff"/></svg><span>1204 Lantern Avenue<br>Cedar Hollow, TX 75000</span></div>
      <div class="contact"><svg width="14" height="14" viewBox="0 0 14 14"><path d="M3 1h3l1 3-2 1a8 8 0 0 0 4 4l1-2 3 1v3a1 1 0 0 1-1 1A11 11 0 0 1 2 2a1 1 0 0 1 1-1z" fill="#d3141b"/></svg><span>(555) 014-2290</span></div>
      <div class="contact"><svg width="14" height="12" viewBox="0 0 14 12"><rect x="1" y="1" width="12" height="10" fill="#d3141b"/><path d="m1 1 6 5 6-5" stroke="#fff" fill="none"/></svg><span>desk@cedarlanterngazette.com</span></div>
    </div>
    <div class="footer__col">
      <div class="footer__head">Social Media</div>
      <div class="social-dots"><span></span><span></span><span></span><span></span><span></span></div>
      <div class="footer__head">Our Newsletter</div>
      <div class="newsletter"><span>Your email</span><b>Go</b></div>
    </div>
  </div>
  <div class="copyright">Copyright © 2015 Cedar Lantern Gazette. All rights reserved.</div>
</footer>

</body>
</html>
```